Wine Label Design

Organization name: Orvell Wine Company

My company is called Orvell Wine Company, I’m a wine importer and wholesaler who distributes wine domestically.

We are about to launch a line of three premium and one sparkling wine that we will wholesale to various retailers, wine stores, and restaurants for re-sale. The wines label will have “Dean Marlowe” I plan on having the labels the same and just changing the varietal as needed. My wine are made from premium grapes and will be marketed as a high end wine. My current label size is 3 1/2" wide by 5" in long and the labels can be on a solid background or transparent.

I would like the first label to be for my Cabernet Sauvignon, California, 2012, 750ML (for the size of the bottle) and ALC 13.8% BY VOL (for the alcohol content).

Colors: I am open to any and all designs that would alter my perception of what will be best!

Further:
Current label is boring and poorly done, so hopefully you designers can come up with something better

Industry/Entity Type

It Company

```html
<!DOCTYPE html>
<html lang="en">
<head>
<meta charset="utf-8">
<title>Orvell Wine – Cabernet Sauvignon Label</title>
<link rel="stylesheet" href="https://fonts.googleapis.com/css2?family=Arimo:wght@700&family=Petit+Formal+Script&display=swap">
<style>
  :root {
    --backdrop: #141212;
    --label-cream: #efe6cf;
    --label-cream-light: #f8f2e2;
    --label-cream-dark: #ddd0b0;
    --band-red: #b4262b;
    --band-red-dark: #8e1a1f;
    --band-gold: #d8b46a;
    --varietal-red: #9c2226;
    --brand-grey: #3a3a3a;
    --brand-red: #cf3a30;
    --ink: #111111;
    --grape-rose: #d99a86;
    --grape-deep: #b86a5a;
  }
  html, body {
    margin: 0;
    padding: 0;
    width: 946px;
    height: 1200px;
    overflow: hidden;
    background: var(--backdrop);
  }
  .canvas {
    position: relative;
    width: 946px;
    height: 1200px;
    background: var(--backdrop);
  }
  .label {
    position: absolute;
    left: 130px;
    top: 150px;
    width: 720px;
    height: 880px;
    background: radial-gradient(ellipse at 50% 55%, var(--label-cream-light) 0%, var(--label-cream) 55%, var(--label-cream-dark) 100%);
    overflow: hidden;
  }
  .band {
    position: absolute;
    left: 0;
    width: 100%;
    height: 56px;
    background: linear-gradient(180deg, var(--band-red) 0%, var(--band-red-dark) 100%);
  }
  .band--top { top: 0; border-bottom: 3px solid var(--band-gold); }
  .band--bottom { bottom: 0; border-top: 3px solid var(--band-gold); }
  .varietal {
    position: absolute;
    left: 60px;
    top: 78px;
    margin: 0;
    font-family: "Petit Formal Script", cursive;
    font-weight: 400;
    font-size: 76px;
    line-height: 88px;
    color: var(--varietal-red);
  }
  .varietal span { display: block; }
  .varietal .line-two { margin-left: -12px; }
  .grape-art {
    position: absolute;
    left: 190px;
    top: 300px;
    width: 320px;
    height: 420px;
  }
  .brand {
    position: absolute;
    right: 40px;
    top: 90px;
    writing-mode: vertical-rl;
    font-family: "Arimo", sans-serif;
    font-weight: 700;
    font-size: 64px;
    letter-spacing: 2px;
    line-height: 1;
    color: var(--brand-grey);
  }
  .brand .brand-word { color: var(--brand-red); margin-top: 36px; }
  .details {
    position: absolute;
    left: 40px;
    top: 742px;
    margin: 0;
    font-family: "Arimo", sans-serif;
    font-weight: 700;
    font-size: 33px;
    color: var(--ink);
  }
</style>
</head>
<body>
<main class="canvas">
  <section class="label">
    <div class="band band--top"></div>

    <h1 class="varietal">
      <span class="line-one">Cabernet</span>
      <span class="line-two">Sauvignon</span>
    </h1>

    <svg class="grape-art" viewBox="0 0 320 420" role="img" aria-label="Illustration of a bunch of grapes on the vine">
      <defs>
        <radialGradient id="grape-fill" cx="50%" cy="40%" r="60%">
          <stop offset="0%" stop-color="var(--grape-rose)"/>
          <stop offset="100%" stop-color="var(--grape-deep)" stop-opacity="0.85"/>
        </radialGradient>
      </defs>
      <ellipse cx="160" cy="210" rx="150" ry="200" fill="url(#grape-fill)"/>
    </svg>

    <div class="brand">
      <span class="brand-name">ORVELL</span>
      <span class="brand-word">WINE</span>
    </div>

    <p class="details">CALIFORNIA,2012,750ML</p>

    <div class="band band--bottom"></div>
  </section>
</main>
</body>
</html>
```